TALVERN CREST LIMITED CALENDAR 2018

We need an innovative calendar design for our company for 2018. to give a brief description of our company:
"Talvern Crest was founded in 2016 to provide a wide range of management consultancy and advisory services to small and medium-sized companies operating in consumer-driven sectors. With more than 300 years of cumulative investment and advisory experience among our sector-focused seasoned professionals, we advise management teams on an aggregate of $850m worth of investments operating in the healthcare, education, food and beverage and logistics sectors within the MENASEA region; the region of our expertise."
We want the design to include the following 12 countries for each month:
1. UAE 2. Saudi Arabia 3. Kuwait 4. Bahrain 5. Qatar 6. Oman 7. Jordan 8. Egypt 9. Singapore 10. Malaysia 11. Thailand 12. Indonesia
The description/design for each month must include each country's economic growth, Per Capita Income, GDP, etc. That is what we wish for the final design for each month to communicate as our company is in to a wide range of Investment management and Advisory Services
Target Market(s)
FINANCIAL SERVICES AND CONSULTING
Industry/Entity Type
Financial Service
Font styles to use
Colors
Designer to choose colors to be used in the design.
Look and feel

```html
<!DOCTYPE html>
<html lang="en">
<head>
<meta charset="utf-8">
<title>Talvern Crest Desk Calendar 2018 – January</title>
<link rel="stylesheet" href="https://fonts.googleapis.com/css2?family=Bebas+Neue&family=Oswald:wght@400;500&family=Roboto:wght@400;500&display=swap">
<style>
  :root {
    --bg: #ffffff;
    --stand: #262626;
    --stand-edge: #1a1a1a;
    --sheet-top: #f4f4f5;
    --sheet-bottom: #d9d9dc;
    --ink: #1c1c1c;
    --navy: #1f2a6e;
    --muted: #8a8a8e;
    --cell: #f7f7f8;
    --cell-line: #b9b9bd;
    --photo: #a5a5a8;
    --photo-dark: #97979a;
    --white: #ffffff;
    --brand: #e8902a;
    --ring: #2a2a2a;
  }
  * { box-sizing: border-box; margin: 0; padding: 0; }
  html, body { width: 1200px; height: 660px; overflow: hidden; background: var(--bg); }
  body { position: relative; font-family: "Roboto", Arial, sans-serif; color: var(--ink); }

  .calendar-stand {
    position: absolute; left: 60px; top: 95px;
    width: 750px; height: 470px;
    background: var(--stand);
    border: 1px solid var(--stand-edge);
  }
  .pen-holder-front {
    position: absolute; left: 810px; top: 285px;
    width: 330px; height: 280px;
    background: var(--stand);
    border: 1px solid var(--stand-edge);
    display: flex; align-items: center; justify-content: center;
  }
  .brand-name {
    font-family: "Oswald", Arial, sans-serif;
    font-weight: 500; font-size: 40px; letter-spacing: 4px;
    color: var(--brand); text-transform: uppercase;
  }

  .binding-rings { position: absolute; top: -14px; height: 28px; }
  .binding-rings.left { left: 70px; }
  .binding-rings.right { left: 480px; }

  .month-sheet {
    position: absolute; left: 25px; top: 12px;
    width: 700px; height: 395px;
    background: linear-gradient(160deg, var(--sheet-top) 0%, var(--sheet-bottom) 100%);
  }

  .month-title {
    position: absolute; left: 30px; top: 40px;
    font-family: "Oswald", Arial, sans-serif; font-weight: 500;
    font-size: 30px; letter-spacing: 1px; line-height: 1.2;
  }
  .year-title {
    position: absolute; left: 245px; top: 40px;
    font-family: "Oswald", Arial, sans-serif; font-weight: 500;
    font-size: 30px; line-height: 1.2;
  }

  .day-grid {
    position: absolute; left: 22px; top: 92px;
    display: grid; grid-template-columns: repeat(7, 36px);
    grid-template-rows: 24px; grid-auto-rows: 32px;
    column-gap: 2px;
  }
  .weekday {
    font-family: "Oswald", Arial, sans-serif; font-size: 13px;
    text-align: center; line-height: 22px; height: 22px;
  }
  .weekday.weekend { color: var(--navy); }
  .date {
    width: 32px; height: 27px; margin: 2px auto 0;
    border: 1px solid var(--cell-line); border-radius: 6px;
    background: var(--cell);
    font-size: 16px; font-weight: 500; line-height: 25px; text-align: center;
  }
  .date.weekend { color: var(--navy); }
  .date.outside { color: #c9c9cc; border-color: #d8d8db; background: transparent; }

  .holiday-note {
    position: absolute; left: 24px; top: 318px;
    font-size: 9px; color: #555;
  }

  .country-photo {
    position: absolute; left: 330px; top: 60px;
    width: 330px; height: 235px;
    border-radius: 20px;
    background: linear-gradient(180deg, var(--photo) 0%, var(--photo-dark) 100%);
  }
  .country-name {
    position: absolute; right: 52px; top: 72px;
    font-family: "Bebas Neue", Arial, sans-serif; font-size: 46px; line-height: 1;
    color: var(--white); letter-spacing: 1px;
  }

  .economy-stats { position: absolute; left: 330px; top: 302px; width: 330px; }
  .stat-row { position: relative; height: 27px; border-bottom: 2px solid var(--navy); margin-bottom: 2px; }
  .stat-label { font-size: 12px; color: var(--muted); line-height: 16px; }
  .stat-value {
    position: absolute; right: 0; bottom: -2px;
    width: 105px; height: 16px;
    background: var(--navy);
    clip-path: polygon(22px 0, 100% 0, 100% 100%, 0 100%);
    color: var(--white); font-size: 11px; font-weight: 500;
    text-align: right; padding-right: 10px; line-height: 16px;
  }

  .address-line {
    position: absolute; left: 95px; top: 418px;
    font-size: 21px; color: var(--white);
  }
  .address-line .leader {
    display: inline-block; width: 460px; margin-left: 6px;
    border-bottom: 3px dotted var(--white); vertical-align: -2px;
  }
</style>
</head>
<body>

<div class="calendar-stand">
  <div class="month-sheet">
    <h1 class="month-title">JANUARY</h1>
    <div class="year-title">2018</div>

    <div class="day-grid">
      <div class="weekday weekend">SUN</div><div class="weekday">MON</div><div class="weekday">TUE</div><div class="weekday">WED</div><div class="weekday">THU</div><div class="weekday">FRI</div><div class="weekday weekend">SAT</div>

      <div class="date outside">31</div><div class="date">1</div><div class="date">2</div><div class="date">3</div><div class="date">4</div><div class="date">5</div><div class="date weekend">6</div>
      <div class="date weekend">7</div><div class="date">8</div><div class="date">9</div><div class="date">10</div><div class="date">11</div><div class="date">12</div><div class="date weekend">13</div>
      <div class="date weekend">14</div><div class="date">15</div><div class="date">16</div><div class="date">17</div><div class="date">18</div><div class="date">19</div><div class="date weekend">20</div>
      <div class="date weekend">21</div><div class="date">22</div><div class="date">23</div><div class="date">24</div><div class="date">25</div><div class="date">26</div><div class="date weekend">27</div>
      <div class="date weekend">28</div><div class="date">29</div><div class="date">30</div><div class="date">31</div><div class="date outside">1</div><div class="date outside">2</div><div class="date outside">3</div>
      <div class="date outside">4</div><div class="date outside">5</div><div class="date outside">6</div><div class="date outside">7</div><div class="date outside">8</div><div class="date outside">9</div><div class="date outside">10</div>
    </div>

    <p class="holiday-note">1 New Year 2018</p>

    <div class="country-photo" role="img" aria-label="Photograph of the Dubai skyline, United Arab Emirates"></div>
    <div class="country-name">UAE</div>

    <div class="economy-stats">
      <div class="stat-row"><span class="stat-label">Economic Growth</span><span class="stat-value">1.7%</span></div>
      <div class="stat-row"><span class="stat-label">Per Capita Income</span><span class="stat-value">$43,000</span></div>
      <div class="stat-row"><span class="stat-label">GDP</span><span class="stat-value">$414 bn</span></div>
    </div>
  </div>

  <svg class="binding-rings left" width="70" height="28" viewBox="0 0 70 28" aria-hidden="true">
    <g fill="none" stroke="var(--ring)" stroke-width="2.5">
      <ellipse cx="8" cy="14" rx="6" ry="9"/><ellipse cx="24" cy="14" rx="6" ry="9"/>
      <ellipse cx="40" cy="14" rx="6" ry="9"/><ellipse cx="56" cy="14" rx="6" ry="9"/>
    </g>
  </svg>
  <svg class="binding-rings right" width="70" height="28" viewBox="0 0 70 28" aria-hidden="true">
    <g fill="none" stroke="var(--ring)" stroke-width="2.5">
      <ellipse cx="8" cy="14" rx="6" ry="9"/><ellipse cx="24" cy="14" rx="6" ry="9"/>
      <ellipse cx="40" cy="14" rx="6" ry="9"/><ellipse cx="56" cy="14" rx="6" ry="9"/>
    </g>
  </svg>

  <p class="address-line">address<span class="leader"></span></p>
</div>

<div class="pen-holder-front">
  <span class="brand-name">Talvern Crest</span>
</div>

</body>
</html>
```